Providing Back Office Solutions to Financial Advisors and Attorney Needs a Business Card Design

Need a Business Card Design that speaks to Financial Advisor and Attorneys. Some of the word that come to mind is Clean/Simple & Futuristic.

Industry/Entity Type

Business

```html
<!DOCTYPE html>
<html lang="en">
<head>
<meta charset="utf-8">
<title>Veridan Back Office Solutions – Business Card</title>
<link href="https://fonts.googleapis.com/css2?family=Open+Sans:wght@400;600;700&display=swap" rel="stylesheet">
<style>
  :root {
    --stage: #1b1c1e;
    --brand-blue: #1f7fc0;
    --brand-blue-dark: #1668a6;
    --brand-blue-light: #2f93d4;
    --paper: #ffffff;
    --ink-on-blue: #ffffff;
    --divider: rgba(255,255,255,0.85);
  }
  * { margin: 0; padding: 0; box-sizing: border-box; }
  html, body {
    width: 1200px; height: 904px; overflow: hidden;
    background: var(--stage);
    font-family: "Open Sans", Arial, sans-serif;
  }
  .stage { position: relative; width: 1200px; height: 904px; }

  .card {
    position: absolute;
    width: 560px; height: 320px;
    border-radius: 2px;
    overflow: hidden;
    box-shadow: 0 18px 40px rgba(0,0,0,0.55);
  }

  /* Back of card */
  .card-back { left: 110px; top: 90px; }
  .card-back .pattern-field {
    position: absolute; inset: 0;
    background: radial-gradient(ellipse at 45% 45%, var(--brand-blue-light), var(--brand-blue) 60%, var(--brand-blue-dark));
  }
  .card-back .wordmark {
    position: absolute; left: 0; right: 0; top: 128px;
    text-align: center; color: var(--ink-on-blue);
  }
  .wordmark .name {
    font-weight: 600; font-size: 38px; letter-spacing: 5px; line-height: 1;
  }
  .wordmark .tagline {
    font-weight: 600; font-size: 11px; letter-spacing: 0.5px; margin-top: 6px;
  }

  /* Front of card */
  .card-front { left: 530px; top: 490px; background: var(--paper); }
  .card-front .logo-area {
    position: absolute; left: 0; right: 0; top: 0; height: 146px;
    display: flex; align-items: center; justify-content: center; gap: 12px;
    color: var(--brand-blue);
  }
  .logo-area .mark {
    width: 34px; height: 34px; background: var(--brand-blue);
  }
  .logo-area .wordmark { text-align: left; }
  .logo-area .name { font-size: 36px; }
  .logo-area .tagline { font-size: 10.5px; }

  .info-band {
    position: absolute; left: 0; right: 0; bottom: 0; height: 174px;
    background: linear-gradient(180deg, var(--brand-blue) 0%, var(--brand-blue-dark) 100%);
    color: var(--ink-on-blue);
  }
  .person {
    position: absolute; right: 290px; top: 82px; text-align: right;
  }
  .person .full-name { font-weight: 700; font-size: 19px; line-height: 1.2; }
  .person .role { font-size: 14px; }
  .info-band .divider {
    position: absolute; left: 290px; top: 22px; width: 1px; height: 118px;
    background: var(--divider);
  }
  .contact {
    position: absolute; left: 306px; top: 22px; font-size: 13.5px; line-height: 1.45;
  }
  .contact .address { margin-bottom: 2px; padding-left: 0; }
  .contact li { list-style: none; display: flex; align-items: center; gap: 8px; }
  .contact svg { width: 12px; height: 12px; flex: none; }
</style>
</head>
<body>
<main class="stage">

  <section class="card card-back" aria-label="Card back">
    <div class="pattern-field" role="img" aria-label="Repeating faint brand-mark pattern in blue tones"></div>
    <div class="wordmark">
      <div class="name">VERIDAN</div>
      <div class="tagline">BACK OFFICE SOLUTIONS</div>
    </div>
  </section>

  <section class="card card-front" aria-label="Card front">
    <div class="logo-area">
      <span class="mark" aria-hidden="true"></span>
      <div class="wordmark">
        <div class="name">VERIDAN</div>
        <div class="tagline">BACK OFFICE SOLUTIONS</div>
      </div>
    </div>

    <div class="info-band">
      <div class="person">
        <div class="full-name">Alan Reyes</div>
        <div class="role">Manager</div>
      </div>
      <span class="divider" aria-hidden="true"></span>
      <ul class="contact">
        <li class="address">12 Harbor Lane, Suite 4<br>Westbrook, CA 90210.</li>
        <li>
          <svg viewBox="0 0 12 12" aria-hidden="true"><path d="M2.5 1l2 2-1 1.5a6 6 0 0 0 4 4L9 7.5l2 2-1.5 1.5C5 11 1 7 1 2.5z" fill="#fff"/></svg>
          +000 1234 5678
        </li>
        <li>
          <svg viewBox="0 0 12 12" aria-hidden="true"><rect x="1" y="2.5" width="10" height="7" fill="#fff"/><path d="M1 2.5l5 4 5-4" stroke="#1f7fc0" fill="none"/></svg>
          hello@veridanbos.com
        </li>
        <li>
          <svg viewBox="0 0 12 12" aria-hidden="true"><circle cx="6" cy="6" r="5" stroke="#fff" fill="none"/><path d="M1 6h10M6 1c-2.5 3-2.5 7 0 10M6 1c2.5 3 2.5 7 0 10" stroke="#fff" fill="none"/></svg>
          www.veridanbos.com
        </li>
      </ul>
    </div>
  </section>

</main>
</body>
</html>
```